Uncoded front page web design for wedding and event planning company

Hi.

I am launching a wedding and event planning company called Silver Fern Gatherings and need a professional and appealing web design.

So, let me explain my company. I am based in Swindon in Wiltshire but the company will plan weddings and events in Oxfordshire, Wiltshire, Berkshire and London.

We will plan weddings, birthdays, conferences, product launches, fashion shows and conventions but the main focus of the website at this stage should be the weddings with all the other occasions being covered under a single 'events' heading.

My contact details for the website should be:
Marion Blake
marion@silverferngatherings.co.uk
01632 960457 / 07700 900583

I'd like the website to feel clean, bright and elegant and be set against a white or off-white background. My logo is purple and I'd therefore like some purple incorporated into the design although feel free to use a more muted purple as my one might be a little bright? I'm also considering whether it would look nice paired with a little of the colour gold - maybe as a font colour in places?? I'll leave you to figure that one out as your design eye will be better than mine but for your reference below is my purple colour and my suggested gold one....

My purple colour is Pantone 2592 C but feel free to use others
My suggested gold I'm looking at is Pantone 14-1041 TCX

I would like to incorporate a Facebook feed in the front page if possible, if it looks right. I'd also like to include a variety of pictures as well so I've included a few in a Dropbox folder which is linked below. Please don't feel obliged to use them all by any means (there's loads!) but you've got a few there to play with. If you find any other royalty free images you'd rather use please go ahead but on the understanding I can have them afterwards!

My logo can be retrieved via this Dropbox link...
You'll notice there are 2 styles of placement. Please feel free to use either to fit in with your design...
https://www.filedrawer-example.com/sh/qk7pa2mwx9rn4lt/BBBKzq8ohPnvve4S03LoPjvb?dl=0

The wedding images I have are in this Dropbox folder...
https://www.filedrawer-example.com/sh/m8wd6rzp2lo4ye1/BBB4kqrXv8nWd7S05JmOgtlp?dl=0

Other than that, it's over to you.... I can't wait to receive your designs :-)

Ooh....finally just to say, as I receive designs in I think I'll notice aspects that I like and don't like and if I feel they'll be useful for other designers, I'll update my brief below. Thanks

BRIEF UPDATE:
Someone asked if I had a tag-line. Could you use "Creating exquisite occasions today for amazing memories tomorrow"

I realise I hadn't explained what I'd like included on my home page so here's some notes to consider....

A welcome to section for me to start narrative about us and our services which has a button that links to our 'about us' page and 'services' page for further information.

A section that nicely illustrates what services we offer whether that be with icons or pictures.

A section with some photos in that would link to our gallery

A section that shows some customer reviews and blog entries that would link to my reviews page and blog to read more.

And finally a contact us section with my details, social media links and site map.

***
I also need to draw attention to where in the UK my services cover. I was therefore thinking perhaps we could use a picture to demonstrate this where it highlights Wiltshire, Oxfordshire, Berkshire and London on a map thereby demonstrating our areas covered. I have found several English county maps when searching on Google but I'm not sure how to highlight the areas I cover (or dull out the areas I don't) so if you have any ideas on this, I'd really like it incorporated. Thanks. (by the way, for those of you not familiar with English counties, the ones I cover are often abbreviated to Wilts, Oxon, Berks, London, so if you find a suitable map with those names on rather than the full names, you'll know what they are!)

I've found an image of the county map which might work well. I was wondering whether we might somehow grey out the counties I don't cover and just keep the ones I do as mentioned above and then crop it into perhaps a shadowed circle? I've attached a screenshot to the brief.
Updates

I've decided on the tag-line "Creating exquisite occasions today for amazing memories tomorrow" so if that could be included somewhere that would be great. I also need to draw attention to where in the UK my services cover. I was therefore thinking perhaps we could use a picture to demonstrate this where it highlights Wiltshire, Oxfordshire, Berkshire and London on a map thereby demonstrating our areas covered. I have found several English county maps when searching on Google but I'm not sure how to highlight the areas I cover (or dull out the areas I don't) so if you have any ideas on this, I'd really like it incorporated. Thanks. Added Wednesday, June 24, 2015

Target Market(s)

Predominately women aged 25-55

Industry/Entity Type

Wedding Planner

Number of Pages Required

1 page

Font styles to use
Sans Serif
Script

Requirements
Nice to have
• I'd like to see how the colour theme of purple and perhaps a little gold (maybe as a font colour) look against a white background. I've mentioned the Pantone colours in the brief above.
• I've attached a screenshot of a webpage with gold writing in and fonts that I like. Perhaps it could give you inspiration?
Should not have
• I really don't like the font QUILLORA so please done use that.

```html
<!DOCTYPE html>
<html lang="en">
<head>
<meta charset="utf-8">
<title>Silver Fern Gatherings – Home</title>
<link rel="stylesheet" href="https://fonts.googleapis.com/css2?family=Lora:ital,wght@0,400;0,700;1,400&family=Raleway:ital,wght@0,400;0,600;1,400&family=Muli:wght@400;700&display=swap">
<style>
:root{
  --gold:#a8895a;
  --gold-light:#f6ddb3;
  --gold-border:#b08a58;
  --purple:#93309f;
  --ink:#333333;
  --muted:#555555;
  --panel:#f2f2f2;
  --panel-line:#d9d9d9;
  --footer:#1f1f1f;
  --footer-bottom:#0c0c0c;
  --footer-text:#d6d6d6;
  --white:#ffffff;
}
*{margin:0;padding:0;box-sizing:border-box}
html,body{width:1200px;height:2866px;overflow:hidden;background:var(--white)}
body{position:relative;font-family:"Muli",sans-serif;color:var(--ink)}
.abs{position:absolute}

/* header */
.brand{left:0;width:1200px;top:52px;display:flex;justify-content:center;align-items:center;gap:16px}
.brand-dot{width:46px;height:46px;border-radius:50%;background:var(--purple)}
.brand-name{font-family:"Lora",serif;font-size:40px;color:var(--purple);font-weight:400}
.header-shade{left:160px;width:880px;top:130px;height:40px;border-radius:50%;box-shadow:0 22px 26px -14px rgba(0,0,0,.12)}
.nav{top:182px;left:0;width:1200px;height:30px;font-family:"Lora",serif;font-size:20px;color:#555;list-style:none}
.nav li{position:absolute;top:0}
.nav .active{color:var(--gold)}

/* hero */
.hero{top:233px;left:0;width:1200px;height:486px;background:linear-gradient(90deg,#e9e9e2 0%,#bfc8a5 22%,#6f7552 40%,#b9a282 58%,#e8dcc0 78%,#f3ead2 100%)}
.hero-panel{left:688px;top:310px;width:401px;height:321px;background:rgba(235,215,175,.72);border-radius:6px;display:flex;flex-direction:column;justify-content:center;align-items:center;text-align:center;font-family:"Lora",serif;font-size:37px;line-height:62px;color:#2c2a26}
.hero-panel strong{font-weight:700}
.hero-arrow{top:441px;width:52px;height:83px;background:rgba(255,255,255,.55)}
.hero-arrow svg{display:block;margin:22px auto}

/* headings */
.section-title{left:0;width:1200px;text-align:center;font-family:"Lora",serif;font-style:italic;font-size:43px;color:var(--gold)}
.ornament{left:574px;width:52px;height:18px;background:var(--gold);border-radius:9px 9px 2px 2px;opacity:.85}

/* welcome */
.welcome-box{left:130px;top:870px;width:940px;height:152px;background:var(--panel);border:1px solid var(--panel-line);display:flex;align-items:center;justify-content:center;padding:0 70px;text-align:center;font-size:15px;line-height:23px;color:var(--ink)}

/* services timeline */
.timeline-line{left:599px;top:1143px;width:3px;height:822px;background:var(--gold)}
.timeline-node{width:84px;height:84px;left:558px;border-radius:50%;border:2px solid var(--gold);background:var(--white);display:flex;align-items:center;justify-content:center}
.timeline-node span{width:54px;height:54px;border-radius:50%;background:#e9d3ee}
.service-card{width:365px;height:187px;background:var(--panel);border:1px solid var(--panel-line);border-radius:4px;padding:28px 36px}
.service-card::after{content:"";position:absolute;top:30px;width:0;height:0;border-top:11px solid transparent;border-bottom:11px solid transparent}
.card-left{text-align:right}
.card-left::after{right:-12px;border-left:12px solid var(--panel)}
.card-right::after{left:-12px;border-right:12px solid var(--panel)}
.service-title{font-family:"Raleway",sans-serif;font-style:italic;font-size:26px;color:var(--gold);margin-bottom:18px}
.service-text{font-size:15px;line-height:23px}
.card-left .service-text{text-align:right}
.btn{background:var(--gold-light);border:1px solid var(--gold-border);font-family:"Lora",serif;color:#3a3026;display:flex;align-items:center;justify-content:center}
.read-more{left:522px;top:1965px;width:155px;height:45px;font-size:21px}

/* testimonial */
.testimonial{left:76px;top:2150px;width:1046px;height:342px;background:var(--panel);border:1px solid var(--panel-line)}
.quote-mark{font-family:"Lora",serif;font-weight:700;font-size:96px;line-height:1;color:var(--gold);top:2172px}
.testimonial-text{left:182px;top:2186px;width:840px;text-align:center;font-size:15px;line-height:24px}
.client-photo{left:550px;top:2279px;width:124px;height:124px;border-radius:50%;border:2px solid var(--gold);background:radial-gradient(circle at 50% 45%,#e8d6c8 0%,#b49482 55%,#f4efe9 100%)}
.client-name{left:0;width:1200px;top:2420px;text-align:center;font-weight:700;font-size:17px;color:#222}

/* footer */
.footer{left:0;top:2559px;width:1200px;height:266px;background:var(--footer)}
.footer-bar{left:0;top:2825px;width:1200px;height:41px;background:var(--footer-bottom);color:var(--footer-text);font-size:15px;text-align:center;line-height:41px}
.footer-bar b{color:var(--gold-light);font-weight:400}
.footer-title{font-family:"Lora",serif;font-size:19px;color:var(--gold-light);top:2578px}
.blog-date{font-size:11px;color:#aaa}
.blog-text{font-size:14px;line-height:19px;color:var(--footer-text)}
.blog-link{font-size:14px;color:var(--white);margin-top:3px}
.blog-divider{left:101px;width:307px;top:2698px;border-top:1px dashed #888}
.news-list{left:453px;top:2605px;list-style:none}
.news-list li{font-size:14px;color:var(--footer-text);height:33.5px}
.news-list li::before{content:"» ";color:var(--gold-light)}
.news-list li.current{color:var(--gold-light)}
.newsletter-text{left:808px;top:2609px;width:320px;font-size:14px;line-height:23px;color:var(--footer-text)}
.field{left:808px;width:302px;height:34px;background:var(--white);font-family:Arial,sans-serif;font-size:13px;color:#555;padding:9px 10px}
.subscribe{left:810px;top:2757px;width:138px;height:39px;font-size:19px}
</style>
</head>
<body>

<header>
  <div class="abs brand"><span class="brand-dot"></span><span class="brand-name">Silver Fern Gatherings</span></div>
  <div class="abs header-shade"></div>
  <ul class="abs nav">
    <li class="active" style="left:274px">HOME</li>
    <li style="left:376px">ABOUT</li>
    <li style="left:487px">SERVICES</li>
    <li style="left:619px">COURSE</li>
    <li style="left:739px">SHOP</li>
    <li style="left:832px">CONTACT</li>
  </ul>
</header>

<section>
  <div class="abs hero" role="img" aria-label="Photo of white lilies and greenery in a soft-focus wedding venue"></div>
  <div class="abs hero-panel"><div>Creating Exquisite<br>Occasions Today For<br><strong>Amazing Memories</strong><br>Tomorrow</div></div>
  <div class="abs hero-arrow" style="left:0"><svg width="14" height="40" viewBox="0 0 14 40"><path d="M12 2 L2 20 L12 38" fill="none" stroke="#777" stroke-width="2"/></svg></div>
  <div class="abs hero-arrow" style="left:1148px"><svg width="14" height="40" viewBox="0 0 14 40"><path d="M2 2 L12 20 L2 38" fill="none" stroke="#777" stroke-width="2"/></svg></div>
</section>

<section>
  <h1 class="abs section-title" style="top:766px">Welcome to Silver Fern</h1>
  <div class="abs ornament" style="top:829px" role="img" aria-label="Small gold flourish"></div>
  <div class="abs welcome-box"><p>Lorem Ipsum is simply dummy text of the printing and typesetting industry. Lorem Ipsum has been the industry's standard dummy text ever since the 1500s, when an unknown printer took a galley of type and scrambled it to make a type specimen book.</p></div>
</section>

<section>
  <div class="abs timeline-line"></div>
  <div class="abs timeline-node" style="top:1059px"><span></span></div>
  <div class="abs timeline-node" style="top:1361px"><span></span></div>
  <div class="abs timeline-node" style="top:1661px"><span></span></div>

  <article class="abs service-card card-left" style="left:182px;top:1145px">
    <h2 class="service-title">Full Planning</h2>
    <p class="service-text">Lorem Ipsum is simply dummy text of the printing and typesetting industry. Lorem Ipsum has been the industry.</p>
  </article>
  <article class="abs service-card card-right" style="left:650px;top:1458px">
    <h2 class="service-title">Styling</h2>
    <p class="service-text">Lorem Ipsum is simply dummy text of the printing and typesetting industry. Lorem Ipsum has been the industry.</p>
  </article>
  <article class="abs service-card card-left" style="left:182px;top:1749px">
    <h2 class="service-title">Budget</h2>
    <p class="service-text">Lorem Ipsum is simply dummy text of the printing and typesetting industry. Lorem Ipsum has been the industry.</p>
  </article>
  <div class="abs btn read-more">READ MORE</div>
</section>

<section>
  <h2 class="abs section-title" style="top:2048px">Our Client Say</h2>
  <div class="abs ornament" style="top:2112px" role="img" aria-label="Small gold flourish"></div>
  <div class="abs testimonial"></div>
  <div class="abs quote-mark" style="left:118px">“</div>
  <div class="abs quote-mark" style="left:1032px">”</div>
  <p class="abs testimonial-text">Lorem Ipsum is simply dummy text of the printing and typesetting industry. Lorem Ipsum has been the industry's standard dummy text ever since the 1500s, when an unknown printer took a galley of type and scrambled it to make a type specimen book.</p>
  <div class="abs client-photo" role="img" aria-label="Portrait photo of the client"></div>
  <p class="abs client-name">- Client Name</p>
</section>

<footer>
  <div class="abs footer"></div>
  <h3 class="abs footer-title" style="left:101px">Blog</h3>
  <div class="abs" style="left:101px;top:2603px;width:310px">
    <p class="blog-date">24 June 2015 by Admin</p>
    <p class="blog-text">Lorem Ipsum is simply dummy text of the print and typesetting industry...</p>
    <p class="blog-link">READ MORE</p>
  </div>
  <div class="abs blog-divider"></div>
  <div class="abs" style="left:101px;top:2716px;width:310px">
    <p class="blog-date">24 June 2015 by Admin</p>
    <p class="blog-text">Lorem Ipsum is simply dummy text of the print and typesetting industry...</p>
    <p class="blog-link">READ MORE</p>
  </div>

  <h3 class="abs footer-title" style="left:453px">Latest News</h3>
  <ul class="abs news-list">
    <li class="current">Lorem Ipsum is simply dummy text</li>
    <li>Lorem Ipsum is simply dummy text</li>
    <li>Lorem Ipsum is simply dummy text</li>
    <li>Lorem Ipsum is simply dummy text</li>
    <li>Lorem Ipsum is simply dummy text</li>
    <li>Lorem Ipsum is simply dummy text</li>
  </ul>

  <h3 class="abs footer-title" style="left:808px">Newsletter</h3>
  <p class="abs newsletter-text">Lorem Ipsum is simply dummy text of the printing and typesetting industry.</p>
  <div class="abs field" style="top:2660px">Name</div>
  <div class="abs field" style="top:2704px">Email</div>
  <div class="abs btn subscribe">SUBSCRIBE</div>

  <div class="abs footer-bar">© <b>SILVER FERN</b> - 2015. All Rights reserved.</div>
</footer>

</body>
</html>
```